Design an Elegant Handbag Brand website

I need a webiste design are looking for ideas for a new theme, color scheme, etc. You come up with the general look and feel of the home page and our team will take it from there.
We're only looking for a one (1) page layout which should be fashionable and graphic intensive, but also include the standard homepage links (about us, see our collections, etc)

Target Market(s)

Our customers are fashionable women looking for an animal friendly and environmentally friendly handbag.

Industry/Entity Type

Business

Number of Pages Required

1 page

Font styles to use
Serif
Sans Serif

Requirements
Must have
• Feel free to modify it with different colors or tweaks as you see fit. We are open to all suggestions.
Nice to have

```html
<!DOCTYPE html>
<html lang="en">
<head>
<meta charset="utf-8">
<title>Maravel Fashions — Handbags</title>
<link href="https://fonts.googleapis.com/css2?family=Montserrat:wght@400;500;600;700;800&family=Playfair+Display:wght@700;800&family=PT+Serif:wght@400;700&display=swap" rel="stylesheet">
<style>
:root{
  --ink:#111111;
  --white:#ffffff;
  --gold:#d4ae3a;
  --gold-deep:#c9a230;
  --muted:#555555;
  --card:#f2f2f2;
  --line:#e6e6e6;
  --mint:#d3e6da;
  --leather:#b06a45;
}
*{box-sizing:border-box;margin:0;padding:0}
html,body{width:1200px;height:4087px;overflow:hidden;background:var(--white)}
body{position:relative;font-family:"PT Serif",Georgia,serif;color:var(--ink)}
.abs{position:absolute}
.sans{font-family:"Montserrat",Arial,sans-serif}

/* top bar */
.topbar{left:0;top:0;width:1200px;height:43px;background:var(--ink);color:var(--white);font:500 13px "Montserrat",Arial,sans-serif}
.topbar .left{left:90px;top:14px}
.topbar .left span{margin:0 14px}
.topbar .right{right:90px;top:14px;display:flex;gap:44px}
.topbar .right i{display:inline-block;width:9px;height:9px;background:var(--white);border-radius:2px;margin-right:7px;vertical-align:-1px}
.mainnav{left:0;top:43px;width:1200px;height:51px;border-bottom:1px solid var(--line);display:flex;gap:0;align-items:center;padding-left:88px;font:400 13px "PT Serif",Georgia,serif;letter-spacing:.3px}
.mainnav a{color:#222;text-decoration:none;margin-right:35px}

/* hero */
.hero{left:0;top:94px;width:1200px;height:639px;background:linear-gradient(90deg,#d5e8dc 0%,#cfe3d6 52%,#b46d48 66%,#a8603f 85%,#c8ddcf 100%)}
.hero-title{left:90px;top:216px;font:800 74px/70px "Playfair Display",Georgia,serif;color:var(--ink)}
.hero-text{left:90px;top:380px;font:400 22px/33px "PT Serif",Georgia,serif;color:#222}
.btn-start{left:90px;top:470px;width:207px;height:59px;border-radius:30px;background:var(--gold);color:var(--white);font:700 20px/59px "PT Serif",Georgia,serif;text-align:center}
.hero-social{left:484px;top:672px;display:flex;gap:34px}
.hero-social span{width:18px;height:18px;border-radius:50%;background:var(--white);opacity:.9}

.section-title{left:0;width:1200px;text-align:center;font:600 47px "Montserrat",Arial,sans-serif;color:var(--ink)}

/* best collection */
.collect{top:917px;width:497px;height:391px;background:var(--card)}
.collect .shape{position:absolute;left:110px;top:25px;width:277px;height:350px;border-radius:30px 30px 18px 18px}
.collect .label{position:absolute;left:0;top:318px;width:100%;text-align:center;font:500 32px "Montserrat",Arial,sans-serif;color:var(--white);letter-spacing:.5px}

/* products */
.product{top:1489px;width:238px;height:362px;background:#f1f1f1}
.product.raised{box-shadow:0 4px 10px rgba(0,0,0,.18)}
.product .photo{position:absolute;left:40px;top:40px;width:158px;height:190px;border-radius:40px 40px 20px 20px}
.product .name{position:absolute;left:14px;top:248px;font:500 18px "Montserrat",Arial,sans-serif;color:#222}
.product .price{position:absolute;left:14px;top:275px;font:400 22px "Montserrat",Arial,sans-serif;color:var(--gold)}
.product .price s{color:#555;font-size:17px;margin-right:8px}
.product .choose{position:absolute;left:16px;top:316px;font:400 12px "PT Serif",Georgia,serif;color:#555}
.product .dots{position:absolute;left:17px;top:338px;display:flex;gap:3px}
.product .dots i{width:8px;height:8px;border-radius:50%}
.tag{position:absolute;top:14px;height:26px;font:700 12px/26px "PT Serif",Georgia,serif;color:var(--white);padding:0 14px 0 10px}
.tag.stock{left:-6px;background:var(--gold-deep);clip-path:polygon(0 0,100% 0,88% 50%,100% 100%,0 100%)}
.tag.sold{right:-6px;background:var(--ink);padding:0 10px 0 18px;clip-path:polygon(0 0,100% 0,100% 100%,0 100%,12% 50%)}
.hover-icons{position:absolute;left:66px;top:100px;width:106px;height:106px}
.hover-icons span{position:absolute;width:42px;height:42px;border-radius:50%}
.arrow{width:50px;height:50px;border-radius:50%;background:var(--white);box-shadow:0 1px 6px rgba(0,0,0,.2);top:1644px}

/* categories */
.cat{overflow:hidden}
.cat .label{position:absolute;left:0;top:50%;width:100%;transform:translateY(-50%);text-align:center;font:600 27px/40px "Montserrat",Arial,sans-serif;color:var(--white);letter-spacing:.3px}

/* reviews */
.review{top:2802px;width:300px;text-align:center}
.review .avatar{width:72px;height:72px;border-radius:50%;margin:0 auto 34px}
.review p{font:400 16px/27px "Montserrat",Arial,sans-serif;color:#222}
.review .who{margin-top:9px;font-weight:500}

/* offer + newsletter */
.offer{left:0;top:3117px;width:601px;height:544px;background:linear-gradient(160deg,#bfc3ca 0%,#d9c7b4 45%,#9ea6b8 70%,#2d3142 100%)}
.offer-title{left:92px;top:3170px;font:500 46px/54px "Montserrat",Arial,sans-serif;color:var(--white)}
.offer-title b{font-weight:800}
.offer-sub{left:92px;top:3293px;font:500 22px "Montserrat",Arial,sans-serif;color:var(--white)}
.offer-link{left:92px;top:3363px;font:500 16px "Montserrat",Arial,sans-serif;color:var(--white);text-decoration:underline}
.newsletter{left:601px;top:3117px;width:599px;height:544px;background:var(--gold)}
.nl-title{left:673px;top:3230px;font:600 45px/52px "Montserrat",Arial,sans-serif;color:var(--white)}
.nl-title small{font-size:33px}
.field{left:673px;width:452px;height:48px;background:var(--white);font:400 15px/48px "PT Serif",Georgia,serif;color:#777;padding-left:19px}
.join{left:673px;top:3492px;width:452px;height:49px;background:var(--ink);color:var(--white);font:600 17px/49px "Montserrat",Arial,sans-serif;text-align:center}

/* footer */
.foot-logo{left:92px;top:3774px;font:700 44px/46px "Playfair Display",Georgia,serif;color:var(--ink)}
.foot-social{left:92px;top:3869px;display:flex;gap:14px}
.foot-social span{width:39px;height:39px;border-radius:50%;border:1.5px solid var(--gold)}
.foot-head{top:3772px;font:500 20px "Montserrat",Arial,sans-serif;color:#222;letter-spacing:.5px}
.foot-list{list-style:none;font:400 13px/28.5px "PT Serif",Georgia,serif;color:#333}
.foot-list.others{line-height:32.5px}
.copy{left:0;top:4045px;width:1200px;text-align:center;font:400 13px "Montserrat",Arial,sans-serif;color:#333}
</style>
</head>
<body>

<header>
  <div class="abs topbar">
    <div class="abs left">Newsletter<span>|</span>Contact us</div>
    <div class="abs right"><div><i></i>Login</div><div><i style="border-radius:50%"></i>MyAccount</div></div>
  </div>
  <nav class="abs mainnav">
    <a>HOME</a><a>ABOUT US</a><a>WOMEN'S HAND BAG COLLECTION</a><a>SUMMER 2020 COLLECTION</a><a>WINTER 2020 COLLECTION</a><a>BLOG</a><a>CONTACT US</a>
  </nav>
</header>

<section>
  <div class="abs hero" role="img" aria-label="Woman holding a tan leather handbag against a mint background"></div>
  <h1 class="abs hero-title">Maravel<br>Fashions</h1>
  <p class="abs hero-text">Lorem ipsum dolor sit amet, consectetur adipiscing elit,<br>sed do eiusmod tempor incididunt</p>
  <div class="abs btn-start">Get Started</div>
  <div class="abs hero-social" aria-label="Social links"><span></span><span></span><span></span><span></span><span></span></div>
</section>

<h2 class="abs section-title" style="top:834px">Best Collection</h2>
<div class="abs collect" style="left:90px">
  <div class="shape" role="img" aria-label="Black leather tote bag" style="background:linear-gradient(180deg,#3a3a3a,#141414)"></div>
  <div class="label">LOREM IPSUM</div>
</div>
<div class="abs collect" style="left:611px">
  <div class="shape" role="img" aria-label="Set of three taupe handbags" style="left:60px;width:380px;background:linear-gradient(180deg,#c3ab90,#9c8068)"></div>
  <div class="label">LOREM IPSUM</div>
</div>

<h2 class="abs section-title" style="top:1412px">New Arrivals</h2>
<div class="abs product" style="left:92px">
  <div class="photo" role="img" aria-label="Yellow handbag" style="background:linear-gradient(180deg,#f3d53a,#d9b70e)"></div>
  <div class="tag stock">In stock</div>
  <div class="name">Product Name</div>
  <div class="price"><s>R150</s>R100</div>
  <div class="choose">Choose Color</div>
  <div class="dots"><i style="background:#d4ae3a"></i><i style="background:#111"></i><i style="background:#d21e1e"></i><i style="background:#e36a1e"></i></div>
</div>
<div class="abs product raised" style="left:352px">
  <div class="photo" role="img" aria-label="Brown checkered handbag" style="background:linear-gradient(180deg,#8a5a34,#5a3820)"></div>
  <div class="hover-icons">
    <span style="left:0;top:0;background:var(--gold)"></span>
    <span style="left:56px;top:0;background:var(--ink)"></span>
    <span style="left:0;top:56px;background:var(--ink)"></span>
    <span style="left:56px;top:56px;background:var(--gold)"></span>
    <svg class="abs" style="left:11px;top:14px" width="20" height="14" viewBox="0 0 20 14"><ellipse cx="10" cy="7" rx="9" ry="6" fill="none" stroke="#fff" stroke-width="2"/><circle cx="10" cy="7" r="2.5" fill="#fff"/></svg>
    <svg class="abs" style="left:68px;top:12px" width="18" height="18" viewBox="0 0 18 18"><path d="M1 2h3l2 9h9l2-7H5" fill="none" stroke="#fff" stroke-width="2"/><circle cx="7" cy="15" r="1.6" fill="#fff"/><circle cx="14" cy="15" r="1.6" fill="#fff"/></svg>
    <svg class="abs" style="left:12px;top:69px" width="18" height="16" viewBox="0 0 18 16"><path d="M9 15 2 8a4 4 0 0 1 7-5 4 4 0 0 1 7 5z" fill="#fff"/></svg>
    <svg class="abs" style="left:68px;top:68px" width="18" height="18" viewBox="0 0 18 18"><circle cx="7" cy="7" r="5" fill="none" stroke="#fff" stroke-width="2"/><path d="M11 11l5 5" stroke="#fff" stroke-width="2.5"/></svg>
  </div>
  <div class="tag stock">In stock</div>
  <div class="name">Product Name</div>
  <div class="price"><s>R150</s>R100</div>
  <div class="choose">Choose Color</div>
  <div class="dots"><i style="background:#d4ae3a"></i><i style="background:#111"></i><i style="background:#d21e1e"></i><i style="background:#e36a1e"></i></div>
</div>
<div class="abs product" style="left:613px">
  <div class="photo" role="img" aria-label="Taupe structured handbag" style="background:linear-gradient(180deg,#9a8782,#6c5a55)"></div>
  <div class="tag sold">Sold Out</div>
  <div class="name">Product Name</div>
  <div class="price"><s>R150</s>R100</div>
  <div class="choose">Choose Color</div>
  <div class="dots"><i style="background:#d4ae3a"></i><i style="background:#111"></i><i style="background:#d21e1e"></i><i style="background:#e36a1e"></i></div>
</div>
<div class="abs product" style="left:873px">
  <div class="photo" role="img" aria-label="Coral pink handbag" style="background:linear-gradient(180deg,#f08585,#dc5f62)"></div>
  <div class="name">Product Name</div>
  <div class="price"><s>R150</s>R100</div>
  <div class="choose">Choose Color</div>
  <div class="dots"><i style="background:#d4ae3a"></i><i style="background:#111"></i><i style="background:#d21e1e"></i><i style="background:#e36a1e"></i></div>
</div>
<div class="abs arrow" style="left:64px"><svg width="50" height="50" viewBox="0 0 50 50"><path d="M27 20l-5 5 5 5" fill="none" stroke="#666" stroke-width="1.5"/></svg></div>
<div class="abs arrow" style="left:1081px"><svg width="50" height="50" viewBox="0 0 50 50"><path d="M23 20l5 5-5 5" fill="none" stroke="#666" stroke-width="1.5"/></svg></div>

<h2 class="abs section-title" style="top:1955px">Categories In HandBag</h2>
<div class="abs cat" style="left:0;top:2038px;width:400px;height:286px;background:linear-gradient(135deg,#5a5a5a,#2e2e2e)" role="img" aria-label="Black barrel bag"><div class="label">BARREL BAG</div></div>
<div class="abs cat" style="left:400px;top:2038px;width:400px;height:286px;background:linear-gradient(135deg,#d88fbd,#7a8aa5 60%,#2a2a2a)" role="img" aria-label="Woman carrying a black frame bag"><div class="label">FRAME BAG</div></div>
<div class="abs cat" style="left:800px;top:2038px;width:400px;height:286px;background:linear-gradient(135deg,#4a2e28,#2b1a17)" role="img" aria-label="Dark croc-textured duffel bag"><div class="label">DUFFEL</div></div>
<div class="abs cat" style="left:0;top:2324px;width:300px;height:285px;background:linear-gradient(135deg,#a48868,#b02a2a 55%,#7a6650)" role="img" aria-label="Woman in red coat with a saddle bag"><div class="label">SADOLEBAG</div></div>
<div class="abs cat" style="left:300px;top:2324px;width:300px;height:285px;background:linear-gradient(180deg,#111,#8e1e1e 55%,#1a1a1a)" role="img" aria-label="Red satchel bag on black"><div class="label">SATCHEL</div></div>
<div class="abs cat" style="left:600px;top:2324px;width:300px;height:285px;background:linear-gradient(135deg,#9aa6b2,#4e5d6e 60%,#1f2a38)" role="img" aria-label="Woman with a navy bucket bag"><div class="label">BUCKET BAG</div></div>
<div class="abs cat" style="left:900px;top:2324px;width:300px;height:285px;background:linear-gradient(135deg,#c7ab8e,#3a3a3a 55%,#d0b9a2)" role="img" aria-label="Black backpack purse"><div class="label">BACKPACK<br>PURSE</div></div>

<h2 class="abs section-title" style="top:2712px">Reviews</h2>
<div class="abs review" style="left:67px">
  <div class="avatar" role="img" aria-label="Reviewer portrait" style="background:linear-gradient(135deg,#e8c9b8,#a87868)"></div>
  <p>Lorem ipsum dolor sit amet,<br>consectetur adipiscing elit, sed do<br>eiusmod tempor incididun</p>
  <p class="who">-Annabrook</p>
</div>
<div class="abs review" style="left:450px">
  <div class="avatar" role="img" aria-label="Reviewer portrait" style="background:linear-gradient(135deg,#f0c43a,#3a3a3a)"></div>
  <p>Lorem ipsum dolor sit amet,<br>consectetur adipiscing elit, sed do<br>eiusmod tempor incididun</p>
  <p class="who">-Annabrook</p>
</div>
<div class="abs review" style="left:831px">
  <div class="avatar" role="img" aria-label="Reviewer portrait" style="background:linear-gradient(135deg,#8a7a70,#3c302c)"></div>
  <p>Lorem ipsum dolor sit amet,<br>consectetur adipiscing elit, sed do<br>eiusmod tempor incididun</p>
  <p class="who">-Annabrook</p>
</div>

<section>
  <div class="abs offer" role="img" aria-label="Woman in striped shirt holding a navy handbag"></div>
  <div class="abs offer-title">Get <b>75%</b><br>Offer</div>
  <div class="abs offer-sub">Womens Handbag</div>
  <div class="abs offer-link">Buy Now</div>
  <div class="abs newsletter"></div>
  <div class="abs nl-title">Join Our Newsletter<br>For <small>Get Discount codes</small></div>
  <div class="abs field" style="top:3368px">User Name</div>
  <div class="abs field" style="top:3430px">Email ID</div>
  <div class="abs join">Join Now</div>
</section>

<footer>
  <div class="abs foot-logo">Maravel<br>Fashions</div>
  <div class="abs foot-social" aria-label="Social links"><span></span><span></span><span></span><span></span><span></span></div>
  <div class="abs foot-head" style="left:451px">LINKS</div>
  <ul class="abs foot-list" style="left:452px;top:3816px"><li>Home</li><li>About Us</li><li>Women's Hand Bag Collection</li><li>Summer 2020 Collection</li><li>Winter 2020 Collection</li></ul>
  <ul class="abs foot-list" style="left:703px;top:3816px"><li>Blog</li><li>Contact Us</li></ul>
  <div class="abs foot-head" style="left:944px">OTHERS</div>
  <ul class="abs foot-list others" style="left:946px;top:3815px"><li>Faq</li><li>Terms &amp; Conditions</li><li>Legal</li></ul>
  <div class="abs copy">© Copyrights.2020.The Company Name.All Rights Reserved</div>
</footer>

</body>
</html>
```